Velora "Glass Tide" single cover

We need a cover for Velora's New upcoming single "Glass Tide"
We have posted some Pictures and logo that we want you to work With. We need you to get her to look good :).The title is "Glass Tide" and is "Velora feat. Dorvo mint rascal"
The songs is a little hiphop/RnB (Marla Q'ish).
You can choose what colour you want for the logo and overall. But we don't want it to be gloomy.
watch www.velora-music.example or www.facebook.com/veloramusic
This is a digital release so we need only front page 12x12cm
Updates
If anyone wants to remove the background from the pictures and be creative that is fine! :)
Industry/Entity Type
Digital
Colors
Designer to choose colors to be used in the design.
Look and feel
Each slider illustrates characteristics of the customer's brand and the style your logo design should communicate.

```html
<!DOCTYPE html>
<html lang="en">
<head>
<meta charset="utf-8">
<title>Velora – Glass Tide</title>
<link rel="stylesheet" href="https://fonts.googleapis.com/css2?family=Montserrat:wght@300;400;600&display=swap">
<style>
  :root {
    --stage: #2a2420;
    --cover-dark: #1c1418;
    --violet: #5b3f86;
    --indigo: #2e2c63;
    --ember: #c8601f;
    --amber: #e39a3e;
    --skin-glow: #d9b39a;
    --gold: #e2b441;
    --text-light: #f1ece6;
  }
  * { margin: 0; padding: 0; box-sizing: border-box; }
  html, body {
    width: 1200px;
    height: 841px;
    overflow: hidden;
    background: var(--stage);
  }
  .canvas {
    position: relative;
    width: 1200px;
    height: 841px;
    display: flex;
    align-items: center;
    justify-content: center;
  }
  .cover {
    position: relative;
    width: 760px;
    height: 760px;
    overflow: hidden;
    background: var(--cover-dark);
    font-family: "Montserrat", sans-serif;
    color: var(--text-light);
  }
  .cover-photo {
    position: absolute;
    inset: 0;
    background:
      radial-gradient(ellipse 38% 46% at 50% 42%, var(--skin-glow) 0%, rgba(160,110,85,0.6) 45%, rgba(0,0,0,0) 80%),
      radial-gradient(ellipse 45% 60% at 88% 55%, var(--ember) 0%, rgba(200,96,31,0) 75%),
      radial-gradient(ellipse 45% 60% at 8% 45%, var(--violet) 0%, rgba(91,63,134,0) 75%),
      linear-gradient(180deg, #3a2a2a 0%, var(--cover-dark) 70%, #140d10 100%);
  }
  .cover-photo::after {
    content: "";
    position: absolute;
    inset: 0;
    background:
      linear-gradient(180deg, rgba(0,0,0,0) 55%, rgba(10,6,10,0.65) 100%),
      linear-gradient(90deg, rgba(46,44,99,0.55) 0%, rgba(0,0,0,0) 30%);
  }
  .featuring {
    position: absolute;
    top: 22px;
    left: 0;
    right: 0;
    text-align: center;
    font-size: 13px;
    font-weight: 600;
    letter-spacing: 0.42em;
    text-transform: uppercase;
  }
  .artist-name {
    position: absolute;
    top: 612px;
    left: 0;
    right: 0;
    text-align: center;
    font-size: 88px;
    font-weight: 600;
    line-height: 1;
    letter-spacing: 0.04em;
    text-transform: lowercase;
    color: var(--gold);
  }
  .single-title {
    position: absolute;
    top: 712px;
    left: 0;
    right: 0;
    text-align: center;
    font-size: 18px;
    font-weight: 300;
    letter-spacing: 0.48em;
    text-transform: uppercase;
  }
</style>
</head>
<body>
  <main class="canvas">
    <section class="cover">
      <div class="cover-photo" role="img" aria-label="Portrait of the singer with long wavy hair, lit by violet light on the left and warm orange light on the right"></div>
      <p class="featuring">Feat. Dorvo mint rascal</p>
      <h1 class="artist-name">Velora</h1>
      <h2 class="single-title">Glass Tide</h2>
    </section>
  </main>
</body>
</html>
```